I need a business card design for a new company that will be doing consulting work around issues of cultural competency, and diversity and inclusion. I would like the design to be crisp and clear with bold but conservative colors and incorporate shades of blue

Target Market(s)

Small businesses, schools, non-profits

Industry/Entity Type

Consulting

Font styles to use
Serif
Sans Serif

Colors
0c5ba6
6b449b
3276b5
0292cd

Requirements
Must have
• A Morrow Venture (name of company)
• Tiru Morrow
• CEO
• tiru@amorrowventure.example
• (215)555-0147

```html
<!DOCTYPE html>
<html lang="en">
<head>
<meta charset="utf-8">
<title>Tiru Morrow — Business Card</title>
<link rel="stylesheet" href="https://fonts.googleapis.com/css2?family=Lato:wght@300;400;700;900&display=swap">
<style>
  :root {
    --page-bg: #ececec;
    --card-blue: #1c7bbd;
    --map-blue: #16609a;
    --text-white: #ffffff;
  }
  * { margin: 0; padding: 0; box-sizing: border-box; }
  html, body {
    width: 1200px;
    height: 586px;
    overflow: hidden;
    background: var(--page-bg);
    font-family: "Lato", "Helvetica Neue", Arial, sans-serif;
  }
  .stage {
    width: 1200px;
    height: 586px;
    display: flex;
    align-items: center;
    justify-content: center;
  }
  .card {
    position: relative;
    width: 900px;
    height: 540px;
    background: var(--card-blue);
    overflow: hidden;
  }
  .world-map {
    position: absolute;
    left: 95px;
    top: 79px;
    width: 771px;
    height: 409px;
    border-radius: 40%;
    background: radial-gradient(ellipse at center, rgba(22, 96, 154, 0.55) 0%, rgba(22, 96, 154, 0.3) 55%, rgba(22, 96, 154, 0) 75%);
  }
  .identity {
    position: absolute;
    left: 0;
    right: 0;
    top: 222px;
    text-align: center;
    color: var(--text-white);
  }
  .person-name {
    font-size: 41px;
    line-height: 1;
    letter-spacing: 0.5px;
  }
  .person-name .given { font-weight: 300; }
  .person-name .family { font-weight: 900; }
  .person-name .role {
    font-size: 25px;
    font-weight: 400;
    margin-left: 12px;
  }
  .contact {
    margin-top: 22px;
    display: flex;
    justify-content: center;
    align-items: center;
    gap: 24px;
    font-size: 20px;
    font-weight: 400;
  }
  .contact-item {
    display: flex;
    align-items: center;
    gap: 8px;
  }
  .contact-item svg { fill: var(--text-white); }
</style>
</head>
<body>
  <main class="stage">
    <section class="card">
      <div class="world-map" role="img" aria-label="Dotted world map in darker blue behind the name"></div>
      <div class="identity">
        <h1 class="person-name">
          <span class="given">TIRU</span> <span class="family">MORROW</span><span class="role">CEO</span>
        </h1>
        <div class="contact">
          <span class="contact-item">
            <svg width="20" height="16" viewBox="0 0 20 16" aria-hidden="true">
              <path d="M1 5c0-2 4-4 9-4s9 2 9 4v2h-4V5c-1-1-3-1.5-5-1.5S6 4 5 5v2H1z"/>
              <path d="M4 8h12l2 7H2z"/>
            </svg>
            (215)555-0147
          </span>
          <span class="contact-item">
            <svg width="19" height="14" viewBox="0 0 19 14" aria-hidden="true">
              <path d="M0 0h19v1.5L9.5 8 0 1.5z"/>
              <path d="M0 3.5l9.5 6.5 9.5-6.5V14H0z"/>
            </svg>
            tiru@amorrowventure.example
          </span>
        </div>
      </div>
    </section>
  </main>
</body>
</html>
```